Re-Design Website

Task Outline:
Re- Web design with call-to-action orientated .
Task Description:
■Our Service
Our service is call Pindrove.
We are a mobile games only cross promotion and advertising platform.
■Reference WebSites
This will be few sites that is doing almost similar service
1.www.graphlune.com
2.www.quonbay.com
3.www.plovrik.net/ (japanese site, but don’t worry about the wordings.)
4.http://zentrawell.com/
■ Little Details
In a nutshell, we are advertising company for mobile games, which offer to show fullscreen ads(interstitial ads), standard banner ads, larger banner ads, icon ads and recommendation ads.
Our current site is at www.pindrove.net. (No copy write job has been done for contents yet, don’t worry about that)
Requirements:
● flat design, play well with white space ( we love the marlowpeak.com design )
● A straight to the point landing image
● All contents are fit in a 1 long page -Once scrolled down to contents. It needs to be very neat and clear on how it deliver the message through images and contents.
● Clean, simple. Reduce wordings; focus on graphic-information to intrigue response.
● We would like to reduce navigation activities and to have an outstanding Call To Action (CTA) button, which to convert user into conversion funnel (example, Learn More, to download our eBooks, Sign Up Now, Join)
● Interesting Vistogram/Chirplet button to build variability.
● Desired user experience, that able to convert information to graphical content. (Like above the fold like Zentrawell.com)
Please refer to a few reference images:
1. *upload a few sushi/ice cream/reon/images for them to use”
Pages to design
1. Landing page
2. About Us
3. Sign in & Sign Up (Must be simple and friendly)
Logo:
We are open to suggestions.
Color preference: (We open for suggestions) ---> WE ARE NOT GOING TO USE ORANGE
● color – change corporate Identity color. The background color can be darker above to fold to make it more stylish.
● 3 tone colors on a web page (something like marlwoPeak.com) → For Example (Refering to Marlow Peak : Main Color : Blue, Base Color : Gray… White, Tone Color : Green) ---> Sure you can play around with it.
● fun and energetic color tone (since we are strongly related with mobile games)
Font:
● clear typography - similar to product identity
● helvetica neue light (currently are using but we are open to suggestion)
Target Market:
● Game publisher
● Game Developer
● Partners: Advertising Agencies, (Business 2 Business)
● ASEAN Countries. ie Taiwan, Japan, China, HK...etc
Deadline:
● 31st December 2013

```html
<!DOCTYPE html>
<html lang="en">
<head>
<meta charset="utf-8">
<title>Pindrove – In-app monetization</title>
<link rel="stylesheet" href="https://fonts.googleapis.com/css2?family=Roboto:wght@300;400;500;700&display=swap">
<style>
:root{
  --stage:#666666;
  --navy:#2e3f55;
  --navy-hero:#34495e;
  --navy-soft:#4f6378;
  --nav-text:#9aa6b5;
  --blue:#3a97d8;
  --red:#e74c3c;
  --white:#ffffff;
  --ink:#222222;
  --heading:#2c3e50;
  --muted:#666b73;
  --yellow:#f1c40f;
}
*{margin:0;padding:0;box-sizing:border-box}
html,body{width:1200px;height:1000px;overflow:hidden;background:var(--stage);font-family:"Roboto",Arial,sans-serif}
.page{position:absolute;left:284px;top:0;width:632px;height:1000px;background:var(--white)}
.abs{position:absolute}
.header{left:0;top:0;width:632px;height:54px;background:var(--navy)}
.logo{left:68px;top:22px;color:var(--white);font-size:22px;font-weight:300;letter-spacing:-0.3px}
.nav a{position:absolute;top:33px;font-size:11px;color:var(--nav-text);text-decoration:none;font-weight:300}
.btn{position:absolute;display:flex;align-items:center;justify-content:center;font-weight:500;color:var(--white);text-decoration:none;border-radius:2px}
.btn-blue{background:var(--blue)}
.btn-red{background:var(--red)}
.btn-outline{border:1.5px solid var(--white)}
.btn-dark{background:var(--navy);font-size:6.5px;border-radius:2px}
.hero{left:0;top:54px;width:632px;height:296px;background:var(--navy-hero)}
.hero-visual{left:111px;top:41px;width:185px;height:255px;border-radius:28px 28px 0 0;background:linear-gradient(160deg,#e8e8e8 0%,#c9a58a 55%,#b98a6c 100%)}
.hero-title{left:312px;top:58px;width:220px;color:var(--white);font-size:22px;font-weight:300;line-height:27px}
.features .feature{position:absolute;top:392px;width:160px;text-align:center}
.feature h3{margin-top:62px;font-size:15px;font-weight:500;color:var(--heading);line-height:19px}
.feature p{margin-top:5px;font-size:8px;line-height:13px;color:var(--ink)}
.feature svg{position:absolute;left:54px;top:0}
.pitch{left:70px;top:567px;width:492px;text-align:center;font-size:15px;font-weight:500;line-height:19px;color:var(--ink)}
.formats{left:0;top:689px;width:632px;height:252px;background:var(--blue)}
.card{position:absolute;top:681px;width:114px;height:201px;background:var(--white);border:1px solid var(--navy);border-radius:3px;text-align:center}
.card-visual{position:absolute;left:3px;top:3px;width:106px;height:92px}
.card h4{position:absolute;left:0;width:112px;font-size:10px;font-weight:500;color:var(--heading);line-height:13px}
.card p{position:absolute;left:6px;top:127px;width:100px;font-size:6.5px;line-height:9.5px;color:var(--muted)}
.card .btn{left:26px;top:173px;width:61px;height:17px}
.footer{left:0;top:941px;width:632px;height:59px;background:var(--navy)}
.copyright{left:74px;top:969px;font-size:6px;color:var(--nav-text)}
.badge{position:absolute;top:955px;width:30px;height:30px;border-radius:50%;background:var(--blue);border:3px solid #d7dde4}
</style>
</head>
<body>
<div class="page">
  <header class="abs header">
    <div class="abs logo">Pindrove</div>
    <nav class="nav">
      <a href="#" style="left:289px">about</a>
      <a href="#" style="left:342px">how it works</a>
      <a href="#" style="left:426px">applications</a>
    </nav>
    <a href="#" class="btn btn-blue" style="left:513px;top:31px;width:50px;height:18px;font-size:7px">Sign up</a>
  </header>

  <section class="abs hero">
    <svg class="abs" style="left:68px;top:116px" width="20" height="40" viewBox="0 0 20 40"><polyline points="18,2 2,20 18,38" fill="none" stroke="var(--navy-soft)" stroke-width="2"/></svg>
    <svg class="abs" style="left:544px;top:116px" width="20" height="40" viewBox="0 0 20 40"><polyline points="2,2 18,20 2,38" fill="none" stroke="var(--navy-soft)" stroke-width="2"/></svg>
    <div class="abs hero-visual" role="img" aria-label="Hand holding a smartphone showing a sushi restaurant game"></div>
    <h1 class="abs hero-title">Welcome to your favourite in-app monetization service</h1>
    <a href="#" class="btn btn-outline" style="left:313px;top:173px;width:92px;height:24px;font-size:9px">Learn more</a>
    <a href="#" class="btn btn-red" style="left:416px;top:173px;width:92px;height:24px;font-size:9px">Sign up</a>
  </section>

  <section class="features">
    <div class="feature" style="left:66px">
      <svg width="52" height="48" viewBox="0 0 52 48" style="left:60px;top:6px" aria-hidden="true">
        <rect x="6" y="0" width="40" height="40" fill="#2c6fb5"/>
        <rect x="9" y="6" width="34" height="31" fill="#f4f4f4"/>
        <text x="26" y="30" text-anchor="middle" font-size="20" font-weight="700" fill="var(--red)" font-family="Roboto,sans-serif">1</text>
      </svg>
      <h3>First day<br>monetization</h3>
      <p>Lorem ipsum dolor sit amet, consectetur adipiscing elit. Cras imperdiet pharetra erat, sed vulputate mauris mattis sed.</p>
    </div>
    <div class="feature" style="left:234px">
      <svg width="52" height="52" viewBox="0 0 52 52" aria-hidden="true">
        <circle cx="26" cy="26" r="26" fill="#2a7fc4"/>
        <path d="M26 26 C20 17 11 17 11 26 C11 35 20 35 26 26 C32 17 41 17 41 26 C41 35 32 35 26 26Z" fill="none" stroke="var(--yellow)" stroke-width="4.5"/>
      </svg>
      <h3>Recurring<br>items</h3>
      <p>Lorem ipsum dolor sit amet, consectetur adipiscing elit. Cras imperdiet pharetra erat, sed vulputate mauris mattis sed.</p>
    </div>
    <div class="feature" style="left:403px">
      <svg width="52" height="52" viewBox="0 0 52 52" aria-hidden="true">
        <clipPath id="dial"><circle cx="26" cy="26" r="26"/></clipPath>
        <g clip-path="url(#dial)">
          <rect x="0" y="0" width="26" height="26" fill="#c0392b"/>
          <rect x="26" y="0" width="26" height="26" fill="#8e44ad"/>
          <rect x="0" y="26" width="26" height="26" fill="#e67e22"/>
          <rect x="26" y="26" width="26" height="26" fill="#27ae60"/>
          <polygon points="16,20 36,20 30,52 22,52" fill="#2a7fc4"/>
        </g>
      </svg>
      <h3>Great<br>customisation</h3>
      <p>Lorem ipsum dolor sit amet, consectetur adipiscing elit. Cras imperdiet pharetra erat, sed vulputate mauris mattis sed.</p>
    </div>
  </section>

  <p class="abs pitch">Lorem ipsum dolor sit amet, consectetur adipiscing elit. Cras imperdiet pharetra erat, sed vulputate mauris mattis sed.</p>
  <a href="#" class="btn btn-blue" style="left:257px;top:624px;width:122px;height:22px;font-size:9px;font-weight:400">Download e-book</a>

  <section class="abs formats"></section>

  <article class="card" style="left:69px">
    <div class="card-visual" role="img" aria-label="Ice cream shop game screen" style="background:linear-gradient(180deg,#f3c6c6,#d9a07f)"></div>
    <h4 style="top:111px">Fullscreen ads</h4>
    <p>Lorem ipsum dolor sit amet, consectetur adipiscing elit. Cras imperdiet pharetra erat, sed vulputate mauris mattis sed.</p>
    <a href="#" class="btn btn-dark">How it works</a>
  </article>
  <article class="card" style="left:195px">
    <div class="card-visual" role="img" aria-label="Sushi game banner artwork" style="height:76px;background:linear-gradient(180deg,#ffffff,#e9b9b0)"></div>
    <h4 style="top:95px">Standard and<br>larger ads</h4>
    <p>Lorem ipsum dolor sit amet, consectetur adipiscing elit. Cras imperdiet pharetra erat, sed vulputate mauris mattis sed.</p>
    <a href="#" class="btn btn-dark">How it works</a>
  </article>
  <article class="card" style="left:322px">
    <div class="card-visual" role="img" aria-label="Game app icon with sushi" style="left:8px;top:8px;width:96px;height:88px;border-radius:12px;background:linear-gradient(160deg,#4fc3c9,#2aa3a8)"></div>
    <h4 style="top:111px">Icon ads</h4>
    <p>Lorem ipsum dolor sit amet, consectetur adipiscing elit. Cras imperdiet pharetra erat, sed vulputate mauris mattis sed.</p>
    <a href="#" class="btn btn-dark">How it works</a>
  </article>
  <article class="card" style="left:449px">
    <div class="card-visual" role="img" aria-label="Ice cream game recommendation artwork" style="background:linear-gradient(180deg,#f7d6dc,#c98a6a)"></div>
    <h4 style="top:111px">Recommandations</h4>
    <p>Lorem ipsum dolor sit amet, consectetur adipiscing elit. Cras imperdiet pharetra erat, sed vulputate mauris mattis sed.</p>
    <a href="#" class="btn btn-dark">How it works</a>
  </article>

  <footer class="abs footer"></footer>
  <div class="abs copyright">Copyright 2014 (c) Pindrove</div>
  <a href="#" class="badge" style="left:272px" aria-label="Vistogram"></a>
  <a href="#" class="badge" style="left:332px" aria-label="Chirplet"></a>
  <a href="#" class="btn btn-outline" style="left:449px;top:962px;width:51px;height:17px;font-size:6.5px">About us</a>
  <a href="#" class="btn btn-blue" style="left:513px;top:962px;width:50px;height:17px;font-size:6.5px">Sign up</a>
</div>
</body>
</html>
```